Werbe-Email-Design
Zielgruppe
Wir sind Dienstleister in der Industrie/ Automobilindustrie. Die Zielgruppe für unsere Werbe-Email sind potenzielle Kunden (möglichst Einkäufer) für unser Produkt (Motorhersteller für DC-Motoren). Da es sich um eine Werbe-Email handelt, soll beim Öffnen möglichst gleich ersichtlich sein, ob das Produkt für den Empfänger brauchbar ist, sodass er in diesem Falle die 'nervige Werbe-Mail' nicht sofort löscht.
Aufgabenstellung
Bei dem 'Newsletter' soll es sich um eine einmalige Werbemail handeln, durch die potenzielle Kunden auf unser Produkt aufmerksam werden und mit uns in Kontakt treten, unsere Website besuchen oder sofort bestellen.
Das Produkt verfolgt einen eher ungewöhnlichen Ansatz, der den potenziellen Kunden eben ansprechen könnte oder nicht, da er damit selbst ein umfangreicheres Produkt anbieten könnte, sollte das in seinem Interesse sein.
Da dies ein neuer Ansatz für den potenziellen Kunden wäre, wird der Empfänger der Email nicht damit rechnen. Deshalb ist wichtig, dass beim Öffnen der Email sofort klar wird, was unser Produkt bietet und wie es unserem Kunden von Nutzen sein kann.
Es handelt sich bei den potenziellen Kunden um Motorhersteller (für DC-Motoren im Fahrzeug, bspw. Fensterheber), die diesen Motor selbst nicht ansteuern. Sie verkaufen diese Motoren also entweder ohne Steuerung oder kaufen die Steuerung von einem Dienstleister. Wir bieten eben diese Steuerung an, allerdings konfigurierbar auf die Anwendung des Kunden, sodass kein weiterer Entwicklungsaufwand entsteht. Der Kunde kann also entweder einen bestehenden Lieferanten für seine Steuerung durch uns ersetzen, da wir in der Lage sind, einen sehr niedrigen Stückpreis zu bieten, oder sein Geschäftsfeld erweitern.
Durch die Email soll sich der Empfänger um diesen Umstand und die Vorteile, die durch unser Produkt für ihn entstehen, bewusstwerden.
Beim Öffnen der Email soll der 'Eye-Catcher'-Bereich zu sehen sein, der den Kunden neugierig machen soll. Hat der Kunde Interesse, soll bei Scrollen mehr Information zu sehen sein.
Dieser 'Eye-Catcher'-Bereich ist in der anhängenden PowerPoint-Datei auf der ersten Seite enthalten. Beim Scrollen sollen die Informationen, die sich auf den nächsten Seiten befinden, zu sehen sein. Des Weiteren soll ein Foto der geöffneten ECU (anhängend) zu sehen sein, mit den Informationen zum Gehäuse, sowie zwei Screenshots der mitgelieferten GUI. Da ..

```html
<!DOCTYPE html>
<html lang="de">
<head>
<meta charset="utf-8">
<title>Lindmark Antriebstechnik – ECU für DC-Motoren</title>
<link href="https://fonts.googleapis.com/css2?family=Lato:wght@400;700;900&family=Poppins:wght@400;500;600&display=swap" rel="stylesheet">
<style>
:root{
  --orange:#f7941d;
  --blue:#0a2bc4;
  --page:#eeeeee;
  --card:#ffffff;
  --ink:#1e1e1e;
  --white:#ffffff;
}
*{box-sizing:border-box;margin:0;padding:0}
html,body{width:1200px;height:2247px;overflow:hidden}
body{background:var(--page);position:relative;font-family:'Lato',sans-serif;color:var(--ink)}
.header{position:absolute;left:0;top:0;width:1200px;height:190px;background:var(--white);display:flex;align-items:center;justify-content:center}
.brand{font-family:'Poppins',sans-serif;font-weight:600;font-size:40px;color:#333;display:flex;align-items:center;gap:18px}
.brand-mark{width:30px;height:30px;border-radius:50%;background:var(--orange)}
.card{position:absolute;left:24px;width:1152px;background:var(--card);border-radius:12px}
.benefits{top:256px;height:662px}
.col-title{font-family:'Lato',sans-serif;font-weight:900;color:var(--orange);font-size:25px;line-height:31px;text-align:center;letter-spacing:.5px}
.col-rule{width:180px;height:1px;background:var(--orange);margin:24px auto 22px}
.col{position:absolute;top:38px;font-size:18px;line-height:34.5px}
.col.tech{left:38px;width:300px}
.col.strat{left:793px;width:330px}
ul{list-style:none}
.dots>li{position:relative;padding-left:26px}
.dots>li::before{content:"";position:absolute;left:4px;top:14px;width:7px;height:7px;border-radius:50%;background:var(--orange)}
.sub>li{position:relative;padding-left:26px}
.sub>li::before{content:"";position:absolute;left:4px;top:14px;width:6px;height:6px;border-radius:50%;border:1.5px solid var(--orange)}
.process{position:absolute;left:408px;top:241px;width:384px;height:692px;background:var(--blue);color:var(--white);padding:40px 36px 0 38px;box-shadow:0 10px 30px rgba(0,0,0,.25)}
.process .col-title{color:var(--white);font-size:24px;line-height:32px}
.process .col-rule{background:var(--white);width:178px;margin:20px auto 18px}
.process li{position:relative;padding-left:22px;font-size:17.5px;line-height:34.5px;font-weight:700;margin-bottom:0}
.process li::before{content:"";position:absolute;left:2px;top:14px;width:7px;height:7px;border-radius:50%;background:var(--white)}
.process b{font-weight:900}
.applications{top:961px;height:392px}
.app-list{position:absolute;left:56px;top:64px;width:588px;text-align:center;font-family:'Poppins',sans-serif;font-weight:600;font-size:23px;line-height:42.5px;color:var(--orange)}
.ecu-photo{position:absolute;left:706px;top:35px;width:412px;height:322px;background:linear-gradient(160deg,#6c7a78 0%,#2f3534 45%,#1e4d2e 70%,#a9b3b4 100%)}
.feature-band{position:absolute;left:24px;top:1374px;width:1152px;height:210px;background:var(--blue);border-radius:10px;font-family:'Poppins',sans-serif;font-weight:500;font-size:24px;color:var(--white)}
.feature{position:absolute;display:flex;align-items:center;gap:14px;line-height:30px}
.feature svg{width:20px;height:20px;flex:none}
.savings{top:1606px;height:617px;font-family:'Poppins',sans-serif;font-size:20.5px;line-height:36px}
.section-title{font-family:'Poppins',sans-serif;font-weight:500;color:var(--orange);font-size:27px;line-height:36px;margin-left:54px}
.savings-body{position:absolute;left:0;top:38px;width:1110px}
.savings .dots>li{padding-left:54px}
.savings .dots>li::before{left:33px;top:15px}
.savings .section-title + ul{margin-top:2px}
.housing-title{margin-top:28px}
</style>
</head>
<body>
<header class="header">
  <div class="brand"><span class="brand-mark"></span>Lindmark Antriebstechnik</div>
</header>

<section class="card benefits">
  <div class="col tech">
    <h2 class="col-title">TECHNISCHE<br>VORTEILE</h2>
    <div class="col-rule"></div>
    <ul class="dots">
      <li>Dank Halbleitertechnologie gegenüber Relais:
        <ul class="sub">
          <li>Leiser</li>
          <li>Kein Verschleiß (Kontaktprellen, Lichtbogenentwicklung), kein Icing</li>
          <li>Sehr präzises Ansprechverhalten</li>
        </ul>
      </li>
      <li>Hohe Dynamik im Lastbereich: bis 19A (Stromspitzen bis 30A)</li>
      <li>Geringer Stromverbrauch:
        <ul class="sub">
          <li>Sleep-Mode: &lt; 100 µA.</li>
          <li>On-Mode: &lt; 100 mA</li>
        </ul>
      </li>
      <li>Robust gegen Umwelteinflüsse</li>
    </ul>
  </div>
  <div class="col strat">
    <h2 class="col-title">STRATEGISCHE<br>VORTEILE</h2>
    <div class="col-rule"></div>
    <ul class="dots">
      <li>Komplettpaket zur Ermittlung Ihrer Systemparameter (Strom-/ Spannungsschwellen, Timingparameter u.v.m.)</li>
      <li>ECU bewährt seit 2010</li>
      <li>HW-Stand 3. Generation</li>
      <li>Zertifiziert nach …</li>
      <li>Keine Basisentwicklung erforderlich</li>
      <li>Minimaler Aufwand bei Applikation durch GUI-Konfigurator</li>
      <li>Made in Germany</li>
      <li>Schneller geht’s nicht</li>
    </ul>
  </div>
</section>

<section class="process">
  <h2 class="col-title">IN WENIGEN TAGEN<br>ZUR FERTIGEN</h2>
  <div class="col-rule"></div>
  <ul>
    <li>Ermitteln Sie Ihre Systemparameter mit unserem <b>Komplettpaket</b> zum Anschluss an <b>Ihren DC-Motor</b></li>
    <li>Per einfachem Mausklick werden Ihre Parameter in unsere <b>fertige Software</b> geladen</li>
    <li>Sie können Ihre Einstellungen innerhalb <b>weniger Minuten testen</b>, bis Sie mit unserer maßgeschneiderten Lösung zufrieden sind</li>
    <li>Wir erstellen das LIN File für Ihre Kommunikation mit dem System Ihres Kunden</li>
    <li>Die <b>fertige ECU</b> ist bereit für Ihre Bestellung</li>
  </ul>
</section>

<section class="card applications">
  <p class="app-list">Fensterheber | elektrisch verstellbare Spiegel | Schiebedach | elektrische Sitzverstellung | Scheibenwischer&nbsp; Waschwasserpumpen | Türverriegelung | Spoilerverstellung | Beschattungssysteme |<br>elektrischer Heckklappenantrieb</p>
  <div class="ecu-photo" role="img" aria-label="Foto der geöffneten ECU: grüne Platine in schwarzem Kunststoffgehäuse"></div>
</section>

<section class="feature-band">
  <div class="feature" style="left:54px;top:46px"><svg viewBox="0 0 20 20"><path d="M2 10.5l5 5L18 4.5" fill="none" stroke="#fff" stroke-width="3"/></svg>Anwendung</div>
  <div class="feature" style="left:54px;top:91px"><svg viewBox="0 0 20 20"><path d="M2 10.5l5 5L18 4.5" fill="none" stroke="#fff" stroke-width="3"/></svg>für DC Bürstenmotoren</div>
  <div class="feature" style="left:54px;top:136px"><svg viewBox="0 0 20 20"><path d="M2 10.5l5 5L18 4.5" fill="none" stroke="#fff" stroke-width="3"/></svg>in einer LIN-Umgebung</div>
  <div class="feature" style="left:574px;top:46px"><svg viewBox="0 0 20 20"><path d="M2 10.5l5 5L18 4.5" fill="none" stroke="#fff" stroke-width="3"/></svg>bei hohem Lastbereich</div>
  <div class="feature" style="left:574px;top:91px"><svg viewBox="0 0 20 20"><path d="M2 10.5l5 5L18 4.5" fill="none" stroke="#fff" stroke-width="3"/></svg>mit schnellen Schaltzeiten</div>
  <div class="feature" style="left:574px;top:136px"><svg viewBox="0 0 20 20"><path d="M2 10.5l5 5L18 4.5" fill="none" stroke="#fff" stroke-width="3"/></svg>präzisen Positionsinformationen.</div>
</section>

<section class="card savings">
  <div class="savings-body">
    <h2 class="section-title">Mit unserer ECU sparen Sie Kosten, da</h2>
    <ul class="dots">
      <li>wir aufgrund eines langjährigen Skaleneffekts einen niedrigen Stückpreis anbieten</li>
      <li>Keine Entwicklungskosten entstehen</li>
      <li>für Sie kaum Aufwand bei der Konfiguration entsteht – unser Entwicklungstool mit Realtime Strom- und Spannungsmessung erleichtert die schnelle Applikation</li>
      <li>Sie von uns ein kostenloses Konfigurationspaket zur Verfügung gestellt bekommen – es fallen für Sie bis zur Bestellung keine Kosten an!</li>
    </ul>
    <h2 class="section-title housing-title">Gehäuse</h2>
    <ul class="dots">
      <li>12-poliger Norvex-Stecker</li>
      <li>2-Komponenten Vergusstechnologie auf Silikonbasis</li>
      <li>IP53</li>
      <li>Material: PA6-GF15</li>
      <li>Einfaches Clip-System zur Befestigung</li>
      <li>Alternatives Gehäuse auf Anfrage</li>
    </ul>
  </div>
</section>
</body>
</html>
```